Creation of a construction/bricklaying business website

Following the template format of "Kestrow 2", the following content would need to be included:
1. Landing page with 3 tiles that go to their own pages.
- Landing page to include background photo and description of services offered.
2. 3 tiles to include:
a) "Contact Us For A Free Quote or Friendly Discussion" Form (middle tile)
b) Case Studies and Testimonials
c) Certifications and Professional Membership
- Design logo to be used from previous ArtQuorum project. Example of logo attached below, please access full JPG files from our account.

Target Market(s)

Prospective clients seeking construction work (bricklaying speciality)

Industry/Entity Type

Residential Construction

Coding

Coded - Design and coding required

Number of Pages Required

4 page

Font styles to use
Sans Serif

Colors

Designer to choose colors to be used in the design.

Requirements
Must have
• Following the template format of "Kestrow 2", the following content would need to be included:
• 1. Landing parent page with 3 tiles that go to the 3 child pages.
• - Landing page to include background photo and description of services offered.
• 2. 3 tiles to include:
• a) "Contact Us For A Free Quote or Friendly Discussion" Form (middle tile)
• b) Case Studies and Testimonials (first tile / left side)
• c) Certifications and Professional Memberships (third tile / right side) (This should include logos of the relevant organisations being displayed. Specifically GLW and the Keel Gate GLW).
• - Design logo to be used from previous ArtQuorum project. Example of logo attached below, please access full JPG files from our account.
Nice to have
• Sleek and modern feel.
• Approachable in terms of how people can contact the company for a quote.
• Traditional pictures to give credibility and comfort around choosing this company.
Should not have
• Cheesy pictures
• Over-complicated
• Simple to use
• Easy URL domain name

```html
<!DOCTYPE html>
<html lang="en">
<head>
<meta charset="utf-8">
<title>R.T. Harlow – Construction</title>
<link href="https://fonts.googleapis.com/css2?family=Poppins:wght@400;500;600;700&family=Open+Sans:wght@400;600&display=swap" rel="stylesheet">
<style>
:root{
  --blue:#1757a8;
  --blue-dark:#0f4590;
  --grey:#626262;
  --ink:#222;
  --text:#555;
  --line:#dcdcdc;
  --white:#fff;
  --footer:#15191d;
  --head-font:"Poppins",sans-serif;
  --body-font:"Open Sans",sans-serif;
}
*{box-sizing:border-box;margin:0;padding:0}
html,body{width:1200px;height:2687px;overflow:hidden}
body{font-family:var(--body-font);color:var(--text);background:var(--white);position:relative}
.wrap{width:780px;margin:0 auto;position:relative}

/* top bar */
.topbar{height:36px;position:relative}
.topbar-strip{position:absolute;right:0;top:0;width:627px;height:36px;background:var(--blue);display:flex;align-items:center;gap:26px;padding-left:0;color:#fff;font-size:12px;font-family:var(--head-font)}
.topbar-strip .item{display:flex;align-items:center;gap:8px}
.topbar-strip .item:first-child{margin-left:0}
.topbar-strip .socials{display:flex;gap:18px;margin-left:8px}
.topbar-strip .dot{width:9px;height:9px;border-radius:50%;background:#fff;display:block}

/* header */
.header{height:68px;background:#fff;box-shadow:0 2px 6px rgba(0,0,0,.08);position:relative;z-index:2}
.header .wrap{display:flex;align-items:center;justify-content:space-between;height:68px}
.brand{display:flex;align-items:center;gap:10px;font-family:var(--head-font);font-weight:700;font-size:30px;color:var(--blue);letter-spacing:-.5px}
.brand .mark{width:14px;height:14px;background:var(--blue)}
.nav{display:flex;gap:22px;font-family:var(--head-font);font-weight:600;font-size:11.5px;color:var(--ink);text-transform:uppercase}
.nav a{color:inherit;text-decoration:none;padding:6px 0}
.nav a.active{border:1px solid var(--line);padding:6px 8px;border-radius:3px}

/* hero */
.hero{position:absolute;top:104px;left:0;width:1200px;height:501px}
.hero-photo{position:absolute;inset:0;background:
  linear-gradient(180deg,rgba(90,140,190,.55) 0%,rgba(90,140,190,0) 25%),
  linear-gradient(90deg,#3e5a2a 0%,#6b4636 22%,#8a5842 45%,#7a5040 65%,#465f2e 85%,#2f4a22 100%);}
.hero-photo::after{content:"";position:absolute;left:0;right:0;bottom:0;height:120px;background:linear-gradient(180deg,rgba(120,110,90,0),#7c735f)}
.hero-banner{position:absolute;left:260px;top:224px;width:684px;height:70px;background:var(--blue);border-left:4px solid #fff;display:flex;align-items:center;padding-left:32px;font-family:var(--head-font);font-weight:600;color:#fff;font-size:28px;letter-spacing:.2px}
.hero-btn{position:absolute;left:295px;top:294px;width:140px;height:37px;background:#1b1b1b;color:#fff;font-family:var(--head-font);font-weight:600;font-size:11.5px;display:flex;align-items:center;justify-content:center;letter-spacing:.5px}
.hero-dots{position:absolute;top:462px;left:0;width:100%;display:flex;justify-content:center;gap:8px}
.hero-dots span{width:12px;height:12px;background:#fff}
.hero-dots span.on{background:var(--blue);outline:2px solid #fff}

/* section titles */
.section-title{font-family:var(--head-font);font-weight:700;font-size:29px;text-align:center;color:var(--ink);letter-spacing:.3px}
.section-title .accent{color:var(--blue)}

/* services */
.services{position:absolute;top:672px;left:0;width:1200px}
.service-grid{display:grid;grid-template-columns:repeat(3,245px);column-gap:22px;row-gap:38px;margin-top:45px}
.service-card{height:314px;position:relative}
.service-top{height:80px;position:relative}
.service-top svg{position:absolute;left:0;bottom:0}
.service-body{height:234px;background:#fff;box-shadow:0 3px 10px rgba(0,0,0,.12);text-align:center;padding-top:2px}
.service-icon{width:72px;height:72px;margin:0 auto;border-radius:6px;background:linear-gradient(135deg,#dbe6f4,#b9cde8)}
.service-name{font-family:var(--head-font);font-weight:600;color:var(--blue);font-size:16px;margin-top:14px}
.service-text{font-size:10px;line-height:1.65;margin:8px 22px 0}
.read-more{display:inline-block;margin-top:14px;background:var(--grey);color:#fff;font-family:var(--head-font);font-weight:600;font-size:10px;padding:9px 20px 8px 24px;letter-spacing:.3px}
.read-more.blue{background:var(--blue)}

/* about */
.about{position:absolute;top:1490px;left:0;width:1200px;height:364px;background:linear-gradient(180deg,#1e5db0,#174f9e);color:#fff;text-align:center}
.about .section-title{color:#fff;padding-top:72px}
.about-lead{font-family:var(--head-font);font-weight:600;font-size:12px;margin-top:26px}
.about-text{width:750px;margin:10px auto 0;font-size:11px;line-height:2.05;color:#e2ebf7}
.about .read-more{background:#fff;color:var(--blue);margin-top:22px;padding:10px 24px 9px 28px}

/* tiles */
.tiles{position:absolute;top:1904px;left:0;width:1200px}
.tile-grid{display:grid;grid-template-columns:repeat(3,245px);column-gap:22px;align-items:start}
.tile{background:#fff;box-shadow:0 3px 10px rgba(0,0,0,.13);text-align:center}
.tile-head{background:var(--blue);color:#fff;font-family:var(--head-font);font-weight:600;font-size:13.5px;line-height:1.2;height:58px;display:flex;align-items:center;justify-content:center;position:relative}
.tile-head::after{content:"";position:absolute;left:50%;bottom:-8px;margin-left:-8px;border:8px solid transparent;border-bottom:0;border-top-color:var(--blue)}
.testimonial{height:340px;padding-top:22px}
.avatar{width:76px;height:76px;border-radius:50%;margin:0 auto;background:linear-gradient(180deg,#c9b29b,#8a6f58);border:3px solid #ececec}
.person{font-family:var(--head-font);font-weight:600;font-size:11px;color:var(--ink);margin-top:10px}
.place{font-size:10px;margin-top:2px}
.stars{color:var(--blue);font-size:10px;letter-spacing:1px}
.quote{font-size:10px;line-height:1.7;margin:14px 24px 0}
.form-tile{height:421px}
.quote-form{padding:14px 14px 0}
.field{height:28px;border:1px solid var(--line);margin-bottom:7px;font-size:10px;color:#444;text-align:left;padding-left:10px;display:flex;align-items:center}
.upload{width:156px;background:#9a9a9a;color:#fff;border:0}
.submit{display:inline-block;background:var(--blue);color:#fff;font-family:var(--head-font);font-weight:600;font-size:10.5px;padding:10px 38px 9px;margin-top:20px}
.certs{height:340px}
.badges{display:grid;grid-template-columns:repeat(2,1fr);row-gap:18px;padding:28px 26px 0}
.badge{height:44px;margin:0 auto}
.badge.b1{width:40px;background:#b3232a}
.badge.b2{width:88px;background:#3f4a52;clip-path:polygon(0 0,100% 0,100% 100%,0 100%)}
.badge.b3{width:76px;background:#2f6bb0;height:34px;margin-top:5px}
.badge.b4{width:96px;background:#2556a0;height:26px;margin-top:9px}
.badge.b5{width:46px;border-radius:50%;background:#c8a233}
.badge.b6{width:46px;border-radius:50%;background:#d8b846}
.certs .read-more{margin-top:24px}

/* footer */
.footer{position:absolute;top:2377px;left:0;width:1200px;height:279px;background:linear-gradient(180deg,#1a2024,#0f1316);color:#c9ced3}
.footer-cols{display:flex;padding-top:42px}
.footer h3{font-family:var(--head-font);font-weight:600;color:#fff;font-size:15px;letter-spacing:.5px;padding-bottom:10px;border-bottom:1px solid #39424a;margin-bottom:14px}
.col-links{width:161px}
.col-contact{width:208px}
.col-news{width:245px}
.col-follow{width:166px}
.links{list-style:none;font-size:10px;line-height:25px;text-transform:uppercase}
.links li::before{content:"› ";color:#fff}
.links li.active{color:#fff;font-weight:600}
.contact-row{display:flex;gap:10px;font-size:10.5px;line-height:1.6;margin-bottom:12px}
.contact-row strong{color:#fff}
.ico{width:20px;height:20px;border-radius:50%;background:var(--blue);flex:none;display:flex;align-items:center;justify-content:center}
.news-text{font-size:10.5px;line-height:1.6}
.news-input{width:188px;height:32px;background:#fff;margin-top:12px;font-size:10px;color:#777;padding-left:10px;display:flex;align-items:center}
.news-btn{display:inline-block;background:var(--blue);color:#fff;font-family:var(--head-font);font-weight:600;font-size:10px;padding:8px 18px;margin-top:14px}
.footer-brand{font-family:var(--head-font);font-weight:700;font-size:26px;color:#d5d9dd;margin-top:26px;display:flex;align-items:center;gap:8px}
.footer-brand .mark{width:12px;height:12px;background:#d5d9dd}
.footer-social{display:flex;gap:8px;margin-top:12px;padding-left:30px}
.footer-social span{width:22px;height:22px;border:1px solid #cfd4d8;border-radius:50%}
.copyright{position:absolute;top:2656px;left:0;width:1200px;height:31px;background:var(--blue);color:#dbe6f4;font-size:10px;display:flex;align-items:center;justify-content:center;letter-spacing:.4px}
</style>
</head>
<body>

<div class="topbar">
  <div class="topbar-strip">
    <span class="item" style="margin-left:40px">
      <svg width="14" height="14" viewBox="0 0 24 24" fill="#fff"><path d="M6.6 10.8a15 15 0 0 0 6.6 6.6l2.2-2.2a1 1 0 0 1 1-.25 11.4 11.4 0 0 0 3.6.6 1 1 0 0 1 1 1V20a1 1 0 0 1-1 1A17 17 0 0 1 3 4a1 1 0 0 1 1-1h3.5a1 1 0 0 1 1 1c0 1.25.2 2.45.6 3.6a1 1 0 0 1-.25 1z"/></svg>
      0160 555 0142</span>
    <span class="item">
      <svg width="15" height="12" viewBox="0 0 24 18" fill="none" stroke="#fff" stroke-width="2"><rect x="1" y="1" width="22" height="16"/><path d="M1 1l11 9 11-9"/></svg>
      info@rtharlow.co.uk</span>
    <span class="socials"><span class="dot"></span><span class="dot"></span><span class="dot"></span></span>
  </div>
</div>

<header class="header">
  <div class="wrap">
    <div class="brand"><span class="mark"></span>R.T. Harlow</div>
    <nav class="nav">
      <a class="active">Home</a><a>About Us</a><a>Services</a><a>Testimonials</a><a>Membership</a><a>Contact Us</a>
    </nav>
  </div>
</header>

<section class="hero">
  <div class="hero-photo" role="img" aria-label="Photograph of a large red-brick family house with chimney, patio and surrounding trees"></div>
  <div class="hero-banner">WE ARE THE BEST CONSTRUCTION EXPERTS</div>
  <div class="hero-btn">GET A QUOTE</div>
  <div class="hero-dots"><span></span><span class="on"></span><span></span></div>
</section>

<section class="services">
  <h2 class="section-title"><span class="accent">OUR</span> SERVICES</h2>
  <div class="wrap">
    <div class="service-grid">
      <article class="service-card">
        <div class="service-top"><svg width="245" height="14"><rect width="122" height="14" fill="#1757a8"/><rect x="122" width="123" height="14" fill="#626262"/></svg></div>
        <div class="service-body"><div class="service-icon" role="img" aria-label="Icon of a new house with plans"></div><h3 class="service-name">New build / New houses</h3><p class="service-text">Lorem ipsum dolor sit amet, consectetuer adipiscing elit, sed diam nonummy nibh euismod tincidunt ut laoreet</p><span class="read-more">READ MORE</span></div>
      </article>
      <article class="service-card">
        <div class="service-top"><svg width="245" height="14"><rect width="122" height="14" fill="#1757a8"/><rect x="122" width="123" height="14" fill="#626262"/></svg></div>
        <div class="service-body"><div class="service-icon" role="img" aria-label="Icon of a trowel and wall"></div><h3 class="service-name">Garden walls</h3><p class="service-text">Lorem ipsum dolor sit amet, consectetuer adipiscing elit, sed diam nonummy nibh euismod tincidunt ut laoreet</p><span class="read-more blue">READ MORE</span></div>
      </article>
      <article class="service-card">
        <div class="service-top"><svg width="245" height="14"><rect width="122" height="14" fill="#1757a8"/><rect x="122" width="123" height="14" fill="#626262"/></svg></div>
        <div class="service-body"><div class="service-icon" role="img" aria-label="Icon of a paint roller"></div><h3 class="service-name">Plastering</h3><p class="service-text">Lorem ipsum dolor sit amet, consectetuer adipiscing elit, sed diam nonummy nibh euismod tincidunt ut laoreet</p><span class="read-more">READ MORE</span></div>
      </article>
      <article class="service-card">
        <div class="service-top"><svg width="245" height="14"><rect width="122" height="14" fill="#1757a8"/><rect x="122" width="123" height="14" fill="#626262"/></svg></div>
        <div class="service-body"><div class="service-icon" role="img" aria-label="Icon of a house with an extension"></div><h3 class="service-name">Extensions</h3><p class="service-text">Lorem ipsum dolor sit amet, consectetuer adipiscing elit, sed diam nonummy nibh euismod tincidunt ut laoreet</p><span class="read-more">READ MORE</span></div>
      </article>
      <article class="service-card">
        <div class="service-top"><svg width="245" height="14"><rect width="122" height="14" fill="#1757a8"/><rect x="122" width="123" height="14" fill="#626262"/></svg></div>
        <div class="service-body"><div class="service-icon" role="img" aria-label="Icon of a brick wall"></div><h3 class="service-name">Brickwork</h3><p class="service-text">Lorem ipsum dolor sit amet, consectetuer adipiscing elit, sed diam nonummy nibh euismod tincidunt ut laoreet</p><span class="read-more">READ MORE</span></div>
      </article>
      <article class="service-card">
        <div class="service-top"><svg width="245" height="14"><rect width="122" height="14" fill="#1757a8"/><rect x="122" width="123" height="14" fill="#626262"/></svg></div>
        <div class="service-body"><div class="service-icon" role="img" aria-label="Icon of stepped groundworks"></div><h3 class="service-name">Groundworks</h3><p class="service-text">Lorem ipsum dolor sit amet, consectetuer adipiscing elit, sed diam nonummy nibh euismod tincidunt ut laoreet</p><span class="read-more">READ MORE</span></div>
      </article>
    </div>
  </div>
</section>

<section class="about" role="img" aria-label="Blue-tinted photograph of a timber house frame under construction">
  <h2 class="section-title">ABOUT US</h2>
  <p class="about-lead">We pride ourselves on attention to detail, pride in our completed project and client satisfaction</p>
  <p class="about-text">Lorem ipsum dolor sit amet, consectetuer adipiscing elit, sed diam nonummy nibh euismod tincidunt ut laoreet dolore magna aliquam erat volutpat. Ut wisi enim ad minim veniam, quis nostrud exerci tation ullamcorper suscipit lobortis nisl ut aliquip ex ea commodo consequat. Duis autem vel eum iriure dolor in hendrerit in vulputate velit esse molestie consequat, vel illum dolore eu feugiat nulla facilisis at vero eros et accumsan et iusto odio dignissim qui blandit praesent luptatum zzril delenit augue duis dolore te feugait nulla facilisi.</p>
  <span class="read-more">READ MORE</span>
</section>

<section class="tiles">
  <div class="wrap">
    <div class="tile-grid">
      <div class="tile testimonial-tile">
        <div class="tile-head">Case Studies<br>and Testimonials</div>
        <div class="testimonial">
          <div class="avatar" role="img" aria-label="Portrait photo of a client"></div>
          <p class="person">Daniel Marsh</p>
          <p class="place">Leeds UK</p>
          <p class="stars">★★★★★</p>
          <p class="quote">Lorem ipsum dolor sit amet, con adipiscing elit. Duis at metus rutrum, tempor massa eu, tristique nisl. Sed sed dapibus</p>
          <span class="read-more blue">READ MORE</span>
        </div>
      </div>
      <div class="tile form-tile">
        <div class="tile-head">Contact Us For A Free Quote<br>or Friendly Discussion</div>
        <form class="quote-form">
          <div class="field">Name:</div>
          <div class="field">Email</div>
          <div class="field">Phone</div>
          <div class="field">Post Code</div>
          <div class="field">Description of the job required</div>
          <div class="field upload">Upload Pictures Of Job Site</div>
          <div class="field">Ideal Budget</div>
          <div class="field">Job Time Start And Completion</div>
          <span class="submit">SUBMIT</span>
        </form>
      </div>
      <div class="tile certs">
        <div class="tile-head">Certifications and<br>Professional Memberships</div>
        <div class="badges">
          <div class="badge b1" role="img" aria-label="GLW membership badge"></div>
          <div class="badge b2" role="img" aria-label="Certification badge"></div>
          <div class="badge b3" role="img" aria-label="Trade association badge"></div>
          <div class="badge b4" role="img" aria-label="Keel Gate GLW badge"></div>
          <div class="badge b5" role="img" aria-label="Inspector award badge"></div>
          <div class="badge b6" role="img" aria-label="Gold star contractor badge"></div>
        </div>
        <span class="read-more blue">READ MORE</span>
      </div>
    </div>
  </div>
</section>

<footer class="footer" role="img" aria-label="Dark photograph of a garden and brickwork behind the footer">
  <div class="wrap footer-cols">
    <div class="col-links">
      <h3>QUICK LINKS</h3>
      <ul class="links"><li class="active">Home</li><li>About Us</li><li>Services</li><li>Testimonials</li><li>Membership</li><li>Contact Us</li></ul>
    </div>
    <div class="col-contact">
      <h3>CONTACT INFO</h3>
      <div class="contact-row"><span class="ico"><svg width="10" height="12" viewBox="0 0 24 30" fill="#fff"><path d="M12 0a10 10 0 0 0-10 10c0 8 10 20 10 20s10-12 10-20A10 10 0 0 0 12 0zm0 14a4 4 0 1 1 0-8 4 4 0 0 1 0 8z"/></svg></span><span><strong>R.T. HARLOW</strong><br>18 Fennimore Lane,<br>Ashgrove, London,<br>United Kingdom<br>N4 9QT</span></div>
      <div class="contact-row"><span class="ico"><svg width="10" height="10" viewBox="0 0 24 24" fill="#fff"><path d="M6.6 10.8a15 15 0 0 0 6.6 6.6l2.2-2.2a1 1 0 0 1 1-.25 11.4 11.4 0 0 0 3.6.6 1 1 0 0 1 1 1V20a1 1 0 0 1-1 1A17 17 0 0 1 3 4a1 1 0 0 1 1-1h3.5a1 1 0 0 1 1 1c0 1.25.2 2.45.6 3.6a1 1 0 0 1-.25 1z"/></svg></span><strong style="color:#fff;line-height:20px">07700 900461</strong></div>
      <div class="contact-row"><span class="ico"><svg width="11" height="8" viewBox="0 0 24 18" fill="none" stroke="#fff" stroke-width="2.5"><rect x="1" y="1" width="22" height="16"/><path d="M1 1l11 9 11-9"/></svg></span><span style="line-height:20px">sales@rtharlow.co.uk</span></div>
    </div>
    <div class="col-news">
      <h3>NEWSLETTER SIGNUP</h3>
      <p class="news-text">For regular consumer updates from R.T. Harlow, sign-up here with your email address.</p>
      <div class="news-input">Enter Email</div>
      <span class="news-btn">SIGN UP</span>
    </div>
    <div class="col-follow">
      <h3>FOLLOW US</h3>
      <div class="footer-brand"><span class="mark"></span>R.T. Harlow</div>
      <div class="footer-social"><span></span><span></span><span></span><span></span></div>
    </div>
  </div>
</footer>
<div class="copyright">© COPYRIGHT 2018 R.T. HARLOW. ALL RIGHTS RESERVED.</div>

</body>
</html>
```